Healthy Meal Delivery Website Needs to be updated, current, fresh and modern

Hi there,

The current website i have is super old and outdated.

I would like a beautiful modern site that has all the same content as the previous except with a a new, modern and trustworthy feel.

The current website is https://pelvarobistro.com/

Target Market(s)

Health Conscious Young Professionals

Industry/Entity Type

Food Service

Font styles to use
Sans Serif

Requirements
Must have
• Modern Trustworthy feel
Should not have
• Anything out dated or cheesy or scammy

```html
<!DOCTYPE html>
<html lang="en">
<head>
<meta charset="utf-8">
<title>Pelvaro Bistro — Healthy Meal Delivery</title>
<link href="https://fonts.googleapis.com/css2?family=Baloo+2:wght@600;700;800&family=Open+Sans:wght@400;600;700&display=swap" rel="stylesheet">
<style>
:root{
  --blue:#1f8fd6;
  --yellow:#f0e614;
  --ink:#1c1c1c;
  --text:#555;
  --footer:#1a1a1a;
  --white:#fff;
  --line:#d9d9d9;
}
*{box-sizing:border-box;margin:0;padding:0}
html,body{width:1200px;height:3557px;overflow:hidden}
body{font-family:"Open Sans",sans-serif;color:var(--text);background:var(--white);position:relative}
.abs{position:absolute}
.brand{display:flex;align-items:center;gap:10px;font-family:"Open Sans",sans-serif;font-weight:700;color:var(--blue);font-size:20px}
.brand-mark{width:18px;height:18px;background:var(--yellow)}
.heading{font-family:"Baloo 2",sans-serif;font-weight:800;color:var(--ink);text-align:center;line-height:1.15}
.heading em{font-style:normal;color:var(--blue)}

/* hero */
.hero{left:0;top:0;width:1200px;height:680px;overflow:hidden}
.hero-photo{position:absolute;inset:0;background:radial-gradient(ellipse at 30% 50%,#b8713d 0%,#8c5a34 25%,#c9c1a6 50%,#e7e2d6 75%,#f4f1ea 100%)}
.hero-photo::after{content:"";position:absolute;inset:0;background:rgba(0,0,0,.12)}
.site-header{left:0;top:0;width:1200px;height:150px;background:linear-gradient(#fff 0%,rgba(255,255,255,.85) 70%,rgba(255,255,255,0) 100%)}
.site-header .brand{position:absolute;left:460px;top:30px}
.header-rule{position:absolute;left:100px;width:1000px;height:1px;background:var(--yellow)}
.nav{position:absolute;left:0;top:104px;width:1200px;display:flex;justify-content:center;gap:34px;font-size:14px;font-weight:600;color:var(--blue)}
.hero-title{left:0;top:312px;width:1200px;text-align:center;font-family:"Baloo 2",sans-serif;font-weight:800;font-size:58px;color:var(--white);letter-spacing:1px;text-shadow:0 2px 8px rgba(0,0,0,.35)}
.hero-curve{left:0;top:520px}
.plan{width:150px;height:150px;border-radius:50%;background:var(--white);box-shadow:0 4px 10px rgba(0,0,0,.25);padding:8px}
.plan-photo{width:100%;height:100%;border-radius:50%}
.plan-label{position:absolute;left:50%;top:64px;transform:translateX(-50%);background:var(--white);padding:2px 10px;font-weight:700;font-size:15px;color:var(--ink);white-space:nowrap}

/* about */
.intro-title{left:0;top:768px;width:1200px;font-size:42px}
.tagline{left:0;top:832px;width:1200px;text-align:center;font-size:14px}
.centered-brand{left:0;width:1200px;display:flex;justify-content:center}
.features{left:100px;top:950px;width:450px}
.feature{padding:0 0 16px;margin-bottom:16px;border-bottom:1px solid var(--line)}
.feature:last-child{border-bottom:none}
.feature h3{font-size:15px;font-weight:700;color:var(--ink);margin-bottom:10px}
.feature p{font-size:14px;line-height:1.75}
.dish-back{left:730px;top:960px;width:370px;height:250px;background:#f1f1f1}
.dish{left:680px;top:998px;width:374px;height:256px;background:radial-gradient(ellipse at 50% 55%,#b54a2a 0%,#6f8d3c 35%,#2e3a2a 70%,#1b1e1c 100%);box-shadow:0 8px 20px rgba(0,0,0,.25)}
.btn{left:522px;top:1330px;width:156px;height:48px;border-radius:24px;background:var(--blue);color:var(--white);font-weight:700;font-size:15px;letter-spacing:1px;display:flex;align-items:center;justify-content:center;gap:12px}

/* delivery */
.delivery-title{left:0;top:1490px;width:1200px;font-size:34px}
.lede{left:0;width:1200px;text-align:center;font-size:14px;line-height:1.9}
.tiles{left:100px;top:1753px;width:1000px;height:236px;display:flex}
.tile{flex:1;position:relative;color:var(--white);text-align:center;padding:36px 26px 0}
.tile.blue{background:linear-gradient(135deg,#2a97d8,#1578b8)}
.tile.yellow{background:linear-gradient(135deg,#eadf10,#cfc40a);color:#2a2a2a}
.tile.framed::after{content:"";position:absolute;inset:6px;border:2px solid rgba(255,255,255,.85)}
.tile svg{display:block;margin:0 auto 22px}
.tile h3{font-size:21px;font-weight:600;margin-bottom:10px}
.tile p{font-size:13px;line-height:1.8}

/* menu */
.menu-title{left:0;top:2098px;width:1200px;font-size:40px}
.slide{box-shadow:0 8px 18px rgba(0,0,0,.3)}
.card{left:460px;top:2358px;width:288px;height:378px;background:var(--white);box-shadow:0 8px 22px rgba(0,0,0,.3)}
.card-photo{height:270px;background:radial-gradient(ellipse at 50% 50%,#d9b07a 0%,#a88a4f 40%,#ece6da 72%,#fff 100%)}
.card h4{text-align:center;font-size:17px;letter-spacing:5px;font-weight:600;color:var(--ink);margin:22px 0 8px}
.card p{text-align:center;font-size:13px;line-height:1.6;padding:0 20px}
.dots{left:580px;top:2782px;display:flex;gap:6px}
.dots span{width:9px;height:9px;border-radius:50%;border:1px solid #888}
.dots span.on{background:var(--blue);border-color:var(--blue)}

/* footer */
.footer-curve{left:0;top:2870px}
.footer{left:0;top:2985px;width:1200px;height:572px;background:var(--footer);color:#e6e6e6}
.col{position:absolute;top:98px;font-size:13.5px;line-height:1.9}
.col h4{font-family:"Baloo 2",sans-serif;font-weight:700;font-size:16px;color:var(--white);margin-bottom:4px}
.col h4::after{content:"";display:block;width:30px;height:3px;background:var(--yellow);margin:4px 0 22px}
.news-item{margin-bottom:14px}
.news-item time{display:block;font-size:11px;font-style:italic;color:#888;line-height:1.2}
.socials{display:flex;gap:20px;margin-top:30px}
.socials span{width:16px;height:16px;border-radius:50%;background:var(--yellow)}
.phone-row{display:flex;gap:16px;align-items:flex-start;margin-top:8px}
.phone-box{width:32px;height:32px;border-radius:6px;background:var(--white);display:flex;align-items:center;justify-content:center;flex:none;margin-top:4px}
.email-field{width:263px;height:42px;background:var(--white);color:#777;font-size:12px;padding:0 18px;display:flex;align-items:center}
.subscribe{width:263px;height:42px;background:var(--yellow);color:var(--ink);font-weight:700;font-size:14px;display:flex;align-items:center;justify-content:center;margin-top:8px}
.copyright{left:0;top:3518px;width:1200px;text-align:center;font-size:12px;color:#ccc}
.copyright a{color:var(--yellow);text-decoration:none}
</style>
</head>
<body>

<section class="hero abs">
  <div class="hero-photo" role="img" aria-label="Grilled shrimp tacos with shredded cabbage and a bowl of chilli salsa"></div>
  <header class="site-header abs">
    <div class="brand"><span class="brand-mark"></span>Pelvaro Bistro</div>
    <div class="header-rule" style="top:94px"></div>
    <nav class="nav">
      <span>Home</span><span>Pelvaro Meal Plans</span><span>Menu</span><span>Pricing</span><span>About</span><span>Press</span><span>Contact</span><span>Sign Up</span><span>Login</span>
    </nav>
    <div class="header-rule" style="top:138px"></div>
  </header>
  <h1 class="hero-title abs">PELVARO BISTRO</h1>
  <svg class="hero-curve abs" width="1200" height="160" viewBox="0 0 1200 160">
    <path d="M0 108 C300 170 700 150 1200 30 L1200 160 L0 160 Z" fill="#fff"/>
    <path d="M0 108 C300 170 700 150 1200 30" fill="none" stroke="#f0e614" stroke-width="9"/>
  </svg>
  <div class="plan abs" style="left:592px;top:470px"><div class="plan-photo" role="img" aria-label="Diet plan plate" style="background:radial-gradient(circle,#c9462f,#6c8d3a 60%,#2b2b2b)"></div><span class="plan-label">Pelvaro Diet</span></div>
  <div class="plan abs" style="left:770px;top:466px"><div class="plan-photo" role="img" aria-label="Vegetable salad plate" style="background:radial-gradient(circle,#7fb04a,#3f6b2a 60%,#dcdcd0)"></div><span class="plan-label">Pelvaro Veggie</span></div>
  <div class="plan abs" style="left:950px;top:466px"><div class="plan-photo" role="img" aria-label="A la carte dishes" style="background:radial-gradient(circle,#c58a4a,#8a5a2e 60%,#e8e0d0)"></div><span class="plan-label">A La Carte</span></div>
</section>

<h2 class="heading intro-title abs">The <em>Pelvaro Diet</em></h2>
<p class="tagline abs">Real foods designed by nature prepared by Pelvaro.</p>
<div class="centered-brand abs" style="top:880px"><div class="brand" style="font-size:16px"><span class="brand-mark" style="width:14px;height:14px"></span>Pelvaro Bistro</div></div>

<div class="features abs">
  <div class="feature"><h3>WHAT YOU GET</h3><p>Pelvaro Diet Delivery provides you with 3 fresh daily meals and 3 snacks delivered to your doorstep before 6am.</p></div>
  <div class="feature"><h3>SELECTION</h3><p>Choose your meals from over 100 delicious entrees,<br>snacks and desserts.</p></div>
  <div class="feature"><h3>LUXURY</h3><p>Enjoy the luxury of having your own personal chef and nutritionist prepare Pelvaro Diet meals for you.</p></div>
</div>
<div class="dish-back abs"></div>
<div class="dish abs" role="img" aria-label="Plated salad with grilled salmon and fresh greens"></div>
<div class="btn abs">SEE ALL <svg width="12" height="12" viewBox="0 0 12 12"><path d="M1 1l5 5-5 5M6 1l5 5-5 5" fill="none" stroke="#fff" stroke-width="2"/></svg></div>

<h2 class="heading delivery-title abs">The <em>Pelvaro Diet Delivers</em> Diet Meals To Your<br>Door In Toronto, Gta And Montreal</h2>
<div class="centered-brand abs" style="top:1604px"><div class="brand" style="font-size:16px"><span class="brand-mark" style="width:14px;height:14px"></span>Pelvaro Bistro</div></div>
<p class="lede abs" style="top:1648px">Our fresh and delicious diet meals and snacks are made with only the best natural ingredients that nourish your body.<br>Why not let us prepare your meals while you lose the weight?</p>

<div class="tiles abs">
  <div class="tile blue framed">
    <svg width="52" height="44" viewBox="0 0 52 44" fill="none" stroke="#fff" stroke-width="2"><rect x="2" y="10" width="48" height="32" rx="3"/><path d="M18 10V4h16v6M26 18v16M18 26h16"/></svg>
    <h3>HEALTHY</h3><p>The Pelvaro Diet is a great way to ensure you are eating all the nutrients you need...</p>
  </div>
  <div class="tile yellow">
    <svg width="48" height="48" viewBox="0 0 48 48" fill="none" stroke="#2a2a2a" stroke-width="2"><circle cx="22" cy="26" r="18"/><circle cx="22" cy="26" r="10"/><path d="M16 26l5 5 22-24"/></svg>
    <h3>CHOICE</h3><p>You can choose your own meals from over 100 tasty entrees...</p>
  </div>
  <div class="tile blue">
    <svg width="50" height="44" viewBox="0 0 50 44" fill="none" stroke="#fff" stroke-width="2"><path d="M25 40L6 21A11 11 0 0 1 25 8a11 11 0 0 1 19 13z"/></svg>
    <h3>FRESH</h3><p>All of our meals are real food, freshly prepared by our in-house...</p>
  </div>
  <div class="tile yellow">
    <svg width="48" height="48" viewBox="0 0 48 48" fill="none" stroke="#2a2a2a" stroke-width="2"><circle cx="18" cy="28" r="7"/><path d="M18 14v5M18 37v5M4 28h5M27 28h5M8 18l4 4M24 34l4 4M8 38l4-4M24 22l4-4"/><circle cx="36" cy="12" r="5"/><path d="M36 3v3M36 18v3M27 12h3M42 12h3"/></svg>
    <h3>CUSTOMIZED</h3><p>Your meals will be delivered fresh to your door, customized for your...</p>
  </div>
</div>

<h2 class="heading menu-title abs">Select From Over <em>100 Menu Items</em></h2>
<div class="centered-brand abs" style="top:2178px"><div class="brand" style="font-size:16px"><span class="brand-mark" style="width:14px;height:14px"></span>Pelvaro Bistro</div></div>
<p class="lede abs" style="top:2226px">You can choose your own meals from over 100 tasty entrees, desserts and snack foods.<br>You can choose your meals online, or we can select your meals for you.</p>

<div class="slide abs" role="img" aria-label="Wrap sandwich" style="left:275px;top:2414px;width:100px;height:266px;background:linear-gradient(135deg,#e8c36a,#c98c3e)"></div>
<div class="slide abs" role="img" aria-label="Green juice and vegetables" style="left:363px;top:2390px;width:100px;height:314px;background:linear-gradient(135deg,#4a5a2a,#9a2a1e)"></div>
<div class="slide abs" role="img" aria-label="Grilled burger" style="left:746px;top:2388px;width:100px;height:316px;background:linear-gradient(135deg,#6a4a2a,#c89a4a)"></div>
<div class="slide abs" role="img" aria-label="Vegetable bowl" style="left:838px;top:2412px;width:88px;height:270px;background:linear-gradient(135deg,#8a3a2a,#4a6a2a)"></div>
<div class="card abs">
  <div class="card-photo" role="img" aria-label="Sliced grilled chicken over salad in a white bowl"></div>
  <h4>SNACK</h4>
  <p>Sed ut perspiciatis unde omnis iste natus error sit voluptatem accusantium</p>
</div>
<div class="dots abs"><span class="on"></span><span></span><span></span></div>

<svg class="footer-curve abs" width="1200" height="120" viewBox="0 0 1200 120">
  <path d="M0 95 C400 40 800 0 1200 14 L1200 120 L0 120 Z" fill="#1a1a1a"/>
  <path d="M0 95 C400 40 800 0 1200 14" fill="none" stroke="#f0e614" stroke-width="9"/>
</svg>
<footer class="footer abs">
  <div class="col" style="left:100px;width:270px;text-align:justify">
    <h4>About Us</h4>
    <p>Pelvaro is the Toronto &amp; Montreal Diet Delivery program based on the Pelvaro Diet™, healthy carbs and the right fats.</p><br>
    <p>We provide you with 3 fresh meals, 2 snacks and a dessert delivered to your door before 6am.</p><br>
    <p>Try our Pelvaro Diet™ delivery plan and start Pelvaro weight loss now!</p>
    <div class="socials"><span aria-label="Social link"></span><span aria-label="Social link"></span><span aria-label="Social link"></span><span aria-label="Social link"></span></div>
  </div>
  <div class="col" style="left:460px;width:270px">
    <h4>Latest News</h4>
    <div class="news-item">Sed ut perspiciatis unde omnis iste natus error sit voluptatem accusantium.<time>28.oct 2017</time></div>
    <div class="news-item">Sed ut perspiciatis unde omnis iste natus error sit voluptatem accusantium.<time>12.oct 2017</time></div>
    <div class="news-item">Sed ut perspiciatis unde omnis iste natus error sit voluptatem accusantium.<time>12.oct 2017</time></div>
    <div class="news-item">Sed ut perspiciatis unde omnis iste natus error sit voluptatem accusantium.<time>12.oct 2017</time></div>
  </div>
  <div class="col" style="left:837px;width:263px">
    <h4>Contact Us</h4>
    <p>410 Linden Row, Suite 12, Harbour District, Toronto, Canada</p>
    <p style="margin-top:6px">hello@pelvarobistro.com</p>
    <div class="phone-row">
      <div class="phone-box"><svg width="18" height="18" viewBox="0 0 24 24"><path d="M6.6 10.8a15 15 0 0 0 6.6 6.6l2.2-2.2a1 1 0 0 1 1-.25 11.4 11.4 0 0 0 3.6.57 1 1 0 0 1 1 1V20a1 1 0 0 1-1 1A17 17 0 0 1 3 4a1 1 0 0 1 1-1h3.5a1 1 0 0 1 1 1c0 1.25.2 2.45.57 3.57a1 1 0 0 1-.25 1z" fill="#1a1a1a"/></svg></div>
      <p>+1 (0)55 0142 7310<br>+1 (0)55 0198 2264</p>
    </div>
    <h4 style="margin-top:18px">Get In Touch</h4>
    <div class="email-field">Email Address</div>
    <div class="subscribe">SUBSCRIBE</div>
  </div>
  <p class="copyright abs" style="top:533px">© 2018 Copyrights.<a>PELVAROBISTRO.COM</a>.All Rights Reserved</p>
</footer>

</body>
</html>
```